Business card design needed

I need a business card for my private practice. I would like to see the designs that use bright blue and white. I would like to see similar designs as to the card below:
http://blog.printvarno.com/2009/designing-a-business-card-with-pv-ks517-template.html
I would like to see the back of the card have room for appointment times. Thank you.

Industry/Entity Type
Business
Contact Information for Business Card
Brightwater Counselling & Wellness Services
Helen Dorsey B.Psychology
Registered Psychologist
Building C, Level 3, 14 Marrow Crescent, Canberra, ACT 2601
T: (02) 6287 5912
F: (02) 6287 5930
info@brightwatercounselling.com.au
www.brightwatercounselling.com.au

```html
<!DOCTYPE html>
<html lang="en">
<head>
<meta charset="utf-8">
<title>Business Card Design – Brightwater Counselling &amp; Wellness Services</title>
<link rel="stylesheet" href="https://fonts.googleapis.com/css2?family=Crimson+Text:wght@400;700&family=Caladea&display=swap">
<style>
  :root {
    --brand-blue: #1fb2e8;
    --brand-tint: #b3d9f3;
    --ink-navy: #18233f;
    --paper: #ffffff;
    --rule-blue: #8ccbee;
    --faint-grey: #eceef0;
    --caption-ink: #111111;
    --card-shadow: 5px 6px 6px rgba(0, 0, 0, 0.28);
  }
  * { box-sizing: border-box; margin: 0; padding: 0; }
  html, body { width: 1200px; height: 900px; overflow: hidden; background: var(--paper); }
  .sheet { position: relative; width: 1200px; height: 900px; background: var(--paper); }

  .sheet-title, .view-caption {
    position: absolute;
    font-family: "Caladea", Georgia, serif;
    font-size: 17px;
    color: var(--caption-ink);
    text-align: center;
    width: 510px;
  }
  .sheet-title { left: 345px; top: 90px; }

  .card {
    position: absolute;
    width: 510px;
    height: 288px;
    overflow: hidden;
    box-shadow: var(--card-shadow);
    font-family: "Crimson Text", Georgia, serif;
  }
  .card--front { background: var(--brand-blue); color: var(--paper); }
  .card--option-1 { left: 76px; top: 148px; }
  .card--option-2 { left: 614px; top: 148px; }
  .card--option-3 { left: 76px; top: 492px; }
  .card--reverse { left: 614px; top: 492px; background: var(--paper); }

  .brand-disc {
    position: absolute;
    left: -40px;
    top: -16px;
    width: 320px;
    height: 320px;
    border-radius: 50%;
    background: var(--brand-tint);
  }

  .practice-name {
    position: absolute;
    left: 88px;
    top: 90px;
    font-size: 16px;
    letter-spacing: 0.2px;
    text-transform: uppercase;
    white-space: nowrap;
  }
  .contact-block { position: absolute; left: 290px; top: 126px; }
  .person-name { font-size: 15.5px; font-weight: 700; text-transform: uppercase; line-height: 18px; }
  .person-title { font-size: 12px; line-height: 16px; margin-top: 2px; }
  .contact-lines { margin-top: 9px; font-size: 12px; line-height: 15.6px; white-space: nowrap; }

  .card--option-2 .contact-block { color: var(--ink-navy); }
  .card--option-3 .practice-name { color: var(--ink-navy); }

  .view-caption--option-1 { left: 76px; top: 448px; }
  .view-caption--option-2 { left: 614px; top: 448px; }
  .view-caption--option-3 { left: 76px; top: 792px; }
  .view-caption--reverse { left: 614px; top: 792px; }

  .reverse-disc {
    position: absolute;
    left: -40px;
    top: -10px;
    width: 300px;
    height: 300px;
    border-radius: 50%;
    background: var(--faint-grey);
  }
  .appointment-tab {
    position: absolute;
    left: 30px;
    top: 0;
    width: 451px;
    height: 70px;
    background: var(--brand-blue);
    opacity: 0.95;
    border-radius: 0 0 20px 20px;
    color: var(--paper);
    font-size: 11px;
    letter-spacing: 9.5px;
    text-align: center;
    padding-top: 36px;
    padding-left: 9px;
  }
  .appointment-form { position: absolute; left: 30px; top: 89px; width: 451px; }
  .form-row {
    display: flex;
    height: 29.5px;
    border-bottom: 1px solid var(--rule-blue);
    align-items: flex-end;
    padding-bottom: 4px;
  }
  .form-row--name { height: 15px; }
  .form-label {
    font-size: 7.5px;
    color: var(--ink-navy);
    text-transform: uppercase;
    width: 225px;
  }
</style>
</head>
<body>
<main class="sheet">
  <h1 class="sheet-title" style="font-weight:400">Business Card Design</h1>

  <section class="card card--front card--option-1">
    <div class="brand-disc" role="img" aria-label="Large light blue brand disc"></div>
    <p class="practice-name">Brightwater Counselling &amp; Wellness Services</p>
    <div class="contact-block">
      <p class="person-name">Helen Dorsey</p>
      <p class="person-title">B. Psychology Registered Psychologist</p>
      <p class="contact-lines">Building C, Level 3, 14 Marrow Crescent<br>Canberra, ACT 2601<br>Tel:&nbsp; (02) 6287 5912<br>Fax: (02) 6287 5930<br>info@brightwatercounselling.com.au<br>www.brightwatercounselling.com.au</p>
    </div>
  </section>
  <p class="view-caption view-caption--option-1">Front Side View: Option 1</p>

  <section class="card card--front card--option-2">
    <div class="brand-disc" role="img" aria-label="Large light blue brand disc"></div>
    <p class="practice-name">Brightwater Counselling &amp; Wellness Services</p>
    <div class="contact-block">
      <p class="person-name">Helen Dorsey</p>
      <p class="person-title">B. Psychology Registered Psychologist</p>
      <p class="contact-lines">Building C, Level 3, 14 Marrow Crescent<br>Canberra, ACT 2601<br>Tel:&nbsp; (02) 6287 5912<br>Fax: (02) 6287 5930<br>info@brightwatercounselling.com.au<br>www.brightwatercounselling.com.au</p>
    </div>
  </section>
  <p class="view-caption view-caption--option-2">Front Side View: Option 2</p>

  <section class="card card--front card--option-3">
    <div class="brand-disc" role="img" aria-label="Large light blue brand disc"></div>
    <p class="practice-name">Brightwater Counselling &amp; Wellness Services</p>
    <div class="contact-block">
      <p class="person-name">Helen Dorsey</p>
      <p class="person-title">B. Psychology Registered Psychologist</p>
      <p class="contact-lines">Building C, Level 3, 14 Marrow Crescent<br>Canberra, ACT 2601<br>Tel:&nbsp; (02) 6287 5912<br>Fax: (02) 6287 5930<br>info@brightwatercounselling.com.au<br>www.brightwatercounselling.com.au</p>
    </div>
  </section>
  <p class="view-caption view-caption--option-3">Front Side View: Option 3</p>

  <section class="card card--reverse">
    <div class="reverse-disc" role="img" aria-label="Faint grey brand disc"></div>
    <p class="appointment-tab">APPOINTMENT CARD</p>
    <div class="appointment-form">
      <div class="form-row form-row--name"><span class="form-label">Name :</span></div>
      <div class="form-row"><span class="form-label">Date | Time :</span><span class="form-label">Date | Time :</span></div>
      <div class="form-row"><span class="form-label">Date | Time :</span><span class="form-label">Date | Time :</span></div>
      <div class="form-row"><span class="form-label">Date | Time :</span><span class="form-label">Date | Time :</span></div>
      <div class="form-row"><span class="form-label">Date | Time :</span><span class="form-label">Date | Time :</span></div>
      <div class="form-row"><span class="form-label">Date | Time :</span><span class="form-label">Date | Time :</span></div>
    </div>
  </section>
  <p class="view-caption view-caption--reverse">Reverse Side View</p>
</main>
</body>
</html>
```